business card for law firm that reflects the web site -www.MarlaQuentby.com. That is pleasant to read

We need a business card for a small law firm. Your company designed our logo - tree of life - which I can provide to the designers. The card should be on both sides. Use the coloring from the web site (www.MarlaQuentby.com) and logo (I have several formats). I am attaching the logo, but not sure what format to use.

First side name of firm: Law Office of M.K. Quentby, P.A. 4819 West Pallisor, Suite 300, Phoenix, AZ 85016, Phone: 602.555.3841, Fax: 602.555.7290, web site: www.MarlaQuentby.com, email: MQuentby@MarlaQuentby.com.
Marla K. Quentby Bankruptcy and Foreclosure Attorney & Counselor.
Back side (perhaps vertical) the logo and then Notes with lines. At the bottom: Proud to help people and small businesses file for bankruptcy protection. We are a debt relief agency.
Updates

I have several versions of the logo. Will be happy to share whatever you need. Added Sunday, April 3, 2016

Target Market(s)

everyone

Industry/Entity Type

Legal

Contact Information for Business Card

I prefer something unique (rounded edges, design that adopts my web site - www.MarlaQuentby.com.

Font styles to use
Serif

Requirements
Must have
• First side name of firm: Law Office of M.K. Quentby, P.A. 4819 West Pallisor, Suite 300, Phoenix, AZ 85016, Phone: 602.555.3841, Fax: 602.555.7290, web site: www.MarlaQuentby.com, email: MQuentby@MarlaQuentby.com.
• Marla K. Quentby Bankruptcy and Foreclosure Attorney & Counselor.
• Back side (perhaps vertical) the logo and then Notes with lines. At the bottom: Proud to help people and small businesses file for bankruptcy protection. We are a debt relief agency.
• Green and brown colors that reflect the web site: www.MarlaQuentby.com
Should not have
• Type so small that older people cannot read.

```html
<!DOCTYPE html>
<html lang="en">
<head>
<meta charset="utf-8">
<title>Law Office of M.K. Quentby, P.A. — Business Card</title>
<link href="https://fonts.googleapis.com/css2?family=Tinos:wght@400;700&display=swap" rel="stylesheet">
<style>
  :root {
    --bg: #e9e6e0;
    --card: #f3f3f0;
    --card-edge: #d9d8d4;
    --brown: #5a2a17;
    --green: #1f4a2a;
    --rule: #a9a9a6;
  }
  * { box-sizing: border-box; margin: 0; padding: 0; }
  html, body { width: 1200px; height: 780px; overflow: hidden; }
  body {
    background: var(--bg);
    font-family: "Tinos", "Times New Roman", serif;
    position: relative;
  }
  .card {
    position: absolute;
    background: linear-gradient(135deg, #f7f7f5 0%, var(--card) 60%, #e9e9e6 100%);
    border-radius: 18px;
    box-shadow: 0 2px 0 var(--card-edge), 0 10px 24px rgba(60, 40, 20, 0.18);
  }

  /* Front */
  .card--front { left: 40px; top: 210px; width: 640px; height: 366px; }
  .social { position: absolute; top: 24px; right: 30px; display: flex; gap: 10px; }
  .social__item {
    display: flex; align-items: center; gap: 5px;
    color: var(--green); font-size: 13px; font-weight: 700;
  }
  .social__dot { width: 14px; height: 14px; background: var(--green); border-radius: 3px; }

  .brand-mark {
    position: absolute; left: 14px; top: 92px;
    display: flex; flex-direction: column; align-items: center; gap: 8px; width: 116px;
  }
  .brand-mark__circle { width: 92px; height: 92px; border-radius: 50%; background: var(--green); }
  .brand-mark__name { color: var(--brown); font-size: 14px; font-weight: 700; white-space: nowrap; }

  .firm { position: absolute; left: 142px; top: 66px; color: var(--brown); }
  .firm__pre { font-size: 21px; font-weight: 700; letter-spacing: 0.5px; text-transform: uppercase; }
  .firm__name { font-size: 44px; font-weight: 700; line-height: 1; text-transform: uppercase; letter-spacing: -0.5px; white-space: nowrap; }
  .firm__name small { font-size: 22px; }

  .attorney { position: absolute; left: 142px; top: 160px; }
  .attorney__name { color: var(--brown); font-size: 22px; font-weight: 700; text-transform: uppercase; letter-spacing: 0.3px; }
  .attorney__title { color: var(--green); font-size: 17px; margin-top: 2px; white-space: nowrap; }

  .contact { position: absolute; left: 142px; top: 232px; list-style: none; color: var(--brown); font-size: 15px; line-height: 22px; }
  .contact__row { display: flex; align-items: center; gap: 8px; white-space: nowrap; }
  .contact__icon { width: 15px; height: 15px; flex: none; }
  .contact__row--web { padding-left: 23px; }

  .address {
    position: absolute; right: 30px; bottom: 30px; text-align: right; font-style: normal;
    color: var(--brown); font-size: 16px; line-height: 22px; white-space: nowrap;
  }

  /* Back */
  .card--back { left: 770px; top: 70px; width: 366px; height: 640px; }
  .back-mark {
    position: absolute; top: 40px; left: 0; right: 0;
    display: flex; flex-direction: column; align-items: center; gap: 10px;
  }
  .back-mark__circle { width: 180px; height: 180px; border-radius: 50%; background: var(--green); }
  .back-mark__name { color: var(--brown); font-size: 18px; font-weight: 700; }
  .note { position: absolute; top: 290px; left: 40px; right: 40px; text-align: center; }
  .note__title { color: var(--brown); font-size: 22px; font-weight: 700; letter-spacing: 1px; text-transform: uppercase; }
  .note__lines { margin-top: 10px; list-style: none; }
  .note__lines li { height: 26px; border-bottom: 1px solid var(--rule); }
  .pledge {
    position: absolute; bottom: 48px; left: 20px; right: 20px; text-align: center;
    color: var(--brown); font-size: 20px; line-height: 26px;
  }
</style>
</head>
<body>

<section class="card card--front" aria-label="Business card front">
  <div class="social">
    <span class="social__item"><span class="social__dot"></span>Friendbook</span>
    <span class="social__item"><span class="social__dot"></span>Chirper</span>
  </div>

  <div class="brand-mark">
    <span class="brand-mark__circle"></span>
    <span class="brand-mark__name">M.K. Quentby</span>
  </div>

  <header class="firm">
    <p class="firm__pre">Law Office of</p>
    <h1 class="firm__name">M.K. Quentby<small>, P.A</small></h1>
  </header>

  <div class="attorney">
    <p class="attorney__name">Marla K. Quentby</p>
    <p class="attorney__title">Bankruptcy and Foreclosure Attorney &amp; Counselor</p>
  </div>

  <ul class="contact">
    <li class="contact__row">
      <svg class="contact__icon" viewBox="0 0 16 16"><rect width="16" height="16" rx="3" fill="#1f4a2a"/><path d="M5 3.5l2 2-1 1.3c.6 1.3 1.6 2.3 2.9 2.9l1.3-1 2 2-1.2 1.6C7.9 12 4 8.1 3.5 4.7z" fill="#fff"/></svg>
      602.555.3841
    </li>
    <li class="contact__row">
      <svg class="contact__icon" viewBox="0 0 16 16"><rect width="16" height="16" rx="3" fill="#1f4a2a"/><rect x="4" y="3" width="8" height="4" fill="#fff"/><rect x="3" y="7.5" width="10" height="5.5" rx="1" fill="#fff"/></svg>
      602.555.7290
    </li>
    <li class="contact__row">
      <svg class="contact__icon" viewBox="0 0 16 16"><rect width="16" height="16" rx="3" fill="#1f4a2a"/><rect x="3" y="4.5" width="10" height="7" fill="#fff"/><path d="M3 4.5l5 4 5-4" fill="none" stroke="#1f4a2a" stroke-width="1"/></svg>
      MQuentby@MarlaQuentby.com
    </li>
    <li class="contact__row contact__row--web">www.MarlaQuentby.com</li>
  </ul>

  <address class="address">
    4819 West Pallisor<br>
    Suite 300, Phoenix, AZ 85016
  </address>
</section>

<section class="card card--back" aria-label="Business card back">
  <div class="back-mark">
    <span class="back-mark__circle"></span>
    <span class="back-mark__name">M.K. Quentby</span>
  </div>

  <div class="note">
    <h2 class="note__title">Note</h2>
    <ul class="note__lines">
      <li></li><li></li><li></li><li></li><li></li>
    </ul>
  </div>

  <p class="pledge">
    Proud to help people and<br>
    small businesses file for<br>
    bankruptcy protection.<br>
    We are a debt relief agency.
  </p>
</section>

</body>
</html>
```